Halvorsen & Twigg Client Brochure

I need a Tri- fold brochure for a Custom cabinet company who has first rate skilled millworkers who custom craft cabinets from kitchens, bathrooms, living room entertainment centers, bedrooms to beautiful custom library's, fireplace mantels as well as garages and basement storage units and shelves. They also have a large selection of in stock mouldings. The company has been in business since 1943.See New logo, photos along with old business card and lets create brochure that's fresh and exciting.

Target Market(s)

Homeowners

Industry/Entity Type

It Company

Requirements
Must have
• Company Logo, Business Address, clear photos etc
Nice to have
• Clean and professional looking brochure.

```html
<!DOCTYPE html>
<html lang="en">
<head>
<meta charset="utf-8">
<title>Halvorsen &amp; Twigg Tri-fold Brochure</title>
<link href="https://fonts.googleapis.com/css2?family=Lato:wght@400;700;900&display=swap" rel="stylesheet">
<style>
:root{
  --bg:#d9d9d9;
  --charcoal:#333436;
  --charcoal-dark:#262729;
  --gold:#c9a03c;
  --gold-light:#dcb95e;
  --paper:#ffffff;
  --ink:#4a4a4a;
  --muted:#8a8a8a;
}
*{margin:0;padding:0;box-sizing:border-box}
html,body{width:857px;height:1200px;overflow:hidden;background:var(--bg);font-family:"Lato",sans-serif;color:var(--ink)}
.sheet{position:absolute;left:29px;width:802px;display:flex;box-shadow:0 4px 14px rgba(0,0,0,.25)}
.sheet--outside{top:23px;height:543px}
.sheet--inside{top:606px;height:565px;background:var(--paper)}
.panel{position:relative;width:267.3px;height:100%;overflow:hidden}
.panel--dark{background:var(--charcoal);color:#e4e4e4}
.panel--light{background:var(--paper)}
.photo{position:absolute;display:block}
.gold-head{color:var(--gold);font-weight:700}
p.body{font-size:7.2px;line-height:1.45}
.weblink{position:absolute;left:0;right:0;height:22px;background:var(--gold);color:#fff;font-size:8px;font-weight:700;text-align:center;line-height:22px;letter-spacing:.5px}

/* outside left */
.intro{position:absolute;left:16px;right:16px;top:18px}
.intro h2{font-size:9.5px;line-height:1.3;margin-bottom:5px}
.brand{position:absolute;left:0;right:0;top:292px;text-align:center}
.brand__mark{display:inline-block;width:12px;height:12px;background:var(--gold);vertical-align:middle;margin-right:6px}
.brand__name{font-size:15px;font-weight:900;color:var(--gold);vertical-align:middle;letter-spacing:.5px}
.brand__sub{font-size:6.5px;letter-spacing:2px;color:var(--gold-light);margin-top:4px}
.features{position:absolute;left:14px;right:14px;top:350px;display:flex;gap:10px}
.feature{flex:1}
.feature svg{display:block;margin-bottom:4px}
.feature p{font-size:6.3px;line-height:1.4;color:#cfcfcf}

/* outside middle */
.copy{position:absolute;left:18px;right:18px;top:16px}
.copy h3{font-size:10px;margin:0 0 5px}
.copy p.body{margin-bottom:6px}
.copy h3.section{font-size:12px;margin-top:10px}
.quote-by{font-size:7px;font-style:italic;color:var(--muted);margin:-3px 0 7px}

/* outside right */
.cover-brand{position:absolute;left:0;right:0;top:300px;text-align:center}
.cover-brand .brand__mark{width:16px;height:16px}
.cover-brand .brand__name{font-size:20px}
.tagline{font-size:7px;letter-spacing:1.2px;color:var(--gold);font-weight:700;margin-top:10px;line-height:1.6}
.address{font-size:7.5px;line-height:1.55;color:var(--ink);margin-top:10px}
.social{position:absolute;left:0;right:0;bottom:0;height:36px;background:var(--charcoal-dark);display:flex;align-items:center;justify-content:center;gap:8px}
.social span.dot{width:14px;height:14px;background:var(--gold);display:block}
.social span.label{font-size:7px;color:#ddd;margin-left:4px}

/* inside left */
.about{position:absolute;left:16px;right:16px}
.about h3{font-size:14px;margin-bottom:5px}
.inside-strip{position:absolute;left:0;right:0;bottom:0;height:10px;background:var(--gold)}
</style>
</head>
<body>

<section class="sheet sheet--outside">
  <!-- inside flap -->
  <div class="panel panel--dark">
    <div class="intro">
      <h2 class="gold-head">Halvorsen &amp; Twigg Custom Cabinets &amp; Mouldings Since 1943</h2>
      <p class="body">All cabinets made here on site. We stock a wide variety of mouldings and build every piece by hand for homes across the bay area.</p>
    </div>
    <div class="photo" style="left:0;top:92px;width:267px;height:186px;background:linear-gradient(160deg,#b7b2a8,#6e6a63 60%,#4a4845)" role="img" aria-label="Photo of the company storefront on a street corner"></div>
    <div class="brand">
      <span class="brand__mark"></span><span class="brand__name">Halvorsen &amp; Twigg</span>
      <div class="brand__sub">CUSTOM CABINETS · MOULDINGS</div>
    </div>
    <div class="features">
      <div class="feature">
        <svg width="14" height="14" viewBox="0 0 14 14"><circle cx="7" cy="7" r="6.5" fill="var(--gold)"/><path d="M4 7.2l2 2 4-4.4" stroke="#fff" stroke-width="1.5" fill="none"/></svg>
        <p>Kitchens, baths and living room entertainment centers built to fit.</p>
      </div>
      <div class="feature">
        <svg width="14" height="14" viewBox="0 0 14 14"><circle cx="7" cy="7" r="6.5" fill="var(--gold)"/><path d="M4 7.2l2 2 4-4.4" stroke="#fff" stroke-width="1.5" fill="none"/></svg>
        <p>Custom libraries, fireplace mantels and bedroom storage.</p>
      </div>
      <div class="feature">
        <svg width="14" height="14" viewBox="0 0 14 14"><circle cx="7" cy="7" r="6.5" fill="var(--gold)"/><path d="M4 7.2l2 2 4-4.4" stroke="#fff" stroke-width="1.5" fill="none"/></svg>
        <p>Garage and basement units, shelves and in-stock mouldings.</p>
      </div>
    </div>
    <div class="weblink" style="bottom:14px">www.halvorsentwigg.com</div>
  </div>

  <!-- back panel -->
  <div class="panel panel--light">
    <div class="copy">
      <h3 class="gold-head">Quality, Reliability, Value</h3>
      <p class="body">We take the time to fully understand our customer's expectations. Every project starts with a visit to your home and ends only when the work is just right for you and your family.</p>
      <h3 class="gold-head section">Testimonials</h3>
      <p class="body">"We love the quality and care. The cabinets arrived on time and the crew was kind and patient with every change we asked for."</p>
      <div class="quote-by">— Anna L., Burlingame</div>
      <p class="body">"The new library wall is the heart of our house. Solid work, fair price and true craftsmen from the first sketch to the final coat."</p>
      <div class="quote-by">— Mark D., Redwood City</div>
      <p class="body">"Our kitchen remodel came out better than we imagined. They matched the old mouldings exactly and left the site spotless each day. We recommend them to all our friends."</p>
      <div class="quote-by">— Lisa &amp; Tom R., Foster City</div>
      <p class="body">"Three generations of our family have used this shop. The mantel they built still looks brand new."</p>
      <div class="quote-by">— Carol S., San Mateo</div>
    </div>
    <div class="weblink" style="bottom:14px">www.halvorsentwigg.com</div>
  </div>

  <!-- front cover -->
  <div class="panel panel--light">
    <div class="photo" style="left:0;top:0;width:267px;height:285px;background:linear-gradient(180deg,#efeeea,#cfcbc3 55%,#8c8478)" role="img" aria-label="Photo of a bright white custom kitchen with tall cabinets"></div>
    <div class="cover-brand">
      <span class="brand__mark"></span><span class="brand__name">Halvorsen &amp; Twigg</span>
      <div class="tagline">QUALITY HEIRLOOM · STOCK MOULDINGS<br>CUSTOM CABINETS · MANTELS</div>
      <div class="address">(650) 555-0148<br>sales@halvorsentwigg.com<br>118 Larkspur Lane<br>San Mateo, CA 94400</div>
    </div>
    <div class="social">
      <span class="dot"></span><span class="dot"></span><span class="label">Visit us online</span>
    </div>
  </div>
</section>

<section class="sheet sheet--inside">
  <div class="panel panel--light">
    <div class="about" style="top:16px">
      <h3 class="gold-head">About us</h3>
      <p class="body">Halvorsen &amp; Twigg is a custom cabinet company run by first rate skilled millworkers who custom craft cabinets for kitchens, bathrooms, living rooms, bedrooms and beautiful custom libraries.</p>
    </div>
    <div class="photo" style="left:16px;top:102px;width:235px;height:110px;background:linear-gradient(90deg,#e8dcc6,#b89a6e 50%,#7d5f3e)" role="img" aria-label="Photo of stacked wood mouldings in the showroom"></div>
    <div class="about" style="top:226px">
      <h3 class="gold-head">Since 1943</h3>
      <p class="body">Halvorsen &amp; Twigg is a trusted family shop serving homeowners for generations. We build fireplace mantels, garage and basement storage units and shelves, and keep a large selection of in-stock mouldings ready for pickup.</p>
    </div>
    <div class="photo" style="left:16px;top:338px;width:235px;height:190px;background:linear-gradient(160deg,#d6d3cc,#9c958a 60%,#6a645b)" role="img" aria-label="Photo of the moulding display racks inside the shop"></div>
    <div class="inside-strip"></div>
  </div>

  <div class="panel panel--light">
    <div class="photo" style="left:4px;top:6px;width:259px;height:180px;background:linear-gradient(160deg,#c9bfae,#8a7b65 60%,#4f4538)" role="img" aria-label="Photo of a kitchen with a large range and wood cabinetry"></div>
    <div class="photo" style="left:4px;top:192px;width:126px;height:100px;background:linear-gradient(160deg,#ddd8cf,#9e968a)" role="img" aria-label="Photo of a built-in cabinet detail"></div>
    <div class="photo" style="left:136px;top:192px;width:127px;height:100px;background:linear-gradient(160deg,#6d655c,#2f2c29)" role="img" aria-label="Photo of a dark wood entertainment center"></div>
    <div class="photo" style="left:4px;top:298px;width:259px;height:247px;background:linear-gradient(170deg,#d0ccc4,#8f8b84 55%,#514e4a)" role="img" aria-label="Photo of a kitchen with dark lower cabinets and an island"></div>
    <div class="inside-strip"></div>
  </div>

  <div class="panel panel--light">
    <div class="photo" style="left:4px;top:6px;width:90px;height:180px;background:linear-gradient(180deg,#e6e3dd,#a9a398)" role="img" aria-label="Photo of a tall white pantry cabinet"></div>
    <div class="photo" style="left:100px;top:6px;width:161px;height:180px;background:linear-gradient(180deg,#f1efeb,#c8c3ba 60%,#8d877d)" role="img" aria-label="Photo of a white hallway with arched doorway and built-ins"></div>
    <div class="photo" style="left:4px;top:192px;width:257px;height:353px;background:linear-gradient(170deg,#e2e0dc,#8e8a85 50%,#3b3937)" role="img" aria-label="Photo of a bathroom vanity with dark cabinets and a white sink"></div>
    <div class="inside-strip"></div>
  </div>
</section>

</body>
</html>
```